Professional and creatice Life Coach - Business Card design

I just relaunched my website and now i a need a correspoonding business card for my task as life coach. My website is www.dlorvan.net as reference. The compass is kind of a symbol for my work, as I help people navigate through their challenging phases in life. The business card should be colorful, but not too playful as I also adress business people. So it sould be creative, but professional (also to suport my other business as Management Consultant)

Target Market(s)

People who want to get teir problems resolved, in business, partnership and other personal realms

Industry/Entity Type

Life Coaching

Contact Information for Business Card

Front side should include Name, Phone number, Email, Website and address

Font styles to use
Sans Serif

Colors
add136

Requirements
Must have
• "Mag. Benedikt Haufmoll" -> Name
"Energetische Praxis" -> Jobtitle (describing my profession as life coach)
colours and style should match my website www.dlorvan.net
Nice to have
• a compass as a symbol

```html
<!DOCTYPE html>
<html lang="de">
<head>
<meta charset="utf-8">
<title>Benedikt Haufmoll – Visitenkarte</title>
<link rel="stylesheet" href="https://fonts.googleapis.com/css2?family=Raleway:wght@300;400&family=Arimo:wght@400;700&display=swap">
<style>
  :root {
    --charcoal: #3a3b37;
    --charcoal-deep: #33342f;
    --lime: #add136;
    --paper: #ffffff;
    --ink: #2e2f2b;
    --backdrop: #e9e7e3;
  }
  * { box-sizing: border-box; margin: 0; padding: 0; }
  html, body { width: 1200px; height: 900px; overflow: hidden; }
  body {
    background: var(--backdrop);
    position: relative;
    font-family: "Arimo", Arial, sans-serif;
  }
  .card {
    position: absolute;
    width: 560px;
    height: 320px;
    overflow: hidden;
    box-shadow: 0 6px 18px rgba(0,0,0,0.18);
  }

  /* Back side */
  .card-back {
    left: 70px; top: 110px;
    background: var(--charcoal);
    display: flex; align-items: center; justify-content: center;
  }
  .card-back__name {
    font-family: "Raleway", Arial, sans-serif;
    font-weight: 300;
    font-size: 46px;
    letter-spacing: 1px;
    color: var(--lime);
  }

  /* Front side */
  .card-front {
    left: 570px; top: 470px;
    background: var(--paper);
  }
  .card-front__swoosh { position: absolute; inset: 0; }
  .identity { position: absolute; left: 42px; top: 70px; }
  .identity__name {
    font-weight: 700; font-size: 19px; color: var(--ink);
  }
  .identity__title {
    font-size: 15px; color: var(--lime); margin-top: 3px;
  }
  .contact {
    position: absolute; left: 42px; top: 160px;
    list-style: none; font-size: 15px; color: var(--ink);
  }
  .contact li { display: flex; align-items: center; gap: 7px; line-height: 20px; }
  .contact svg { width: 13px; height: 13px; fill: var(--ink); flex: none; }
  .contact .accent { color: var(--lime); }
  .address {
    position: absolute; left: 55px; top: 232px;
    font-size: 15px; line-height: 20px; color: var(--ink);
  }
  .wordmark {
    position: absolute; right: 40px; top: 54px;
    display: flex; align-items: center; gap: 8px;
  }
  .wordmark__dot {
    width: 16px; height: 16px; border-radius: 50%; background: var(--lime);
  }
  .wordmark__name {
    font-weight: 700; font-size: 24px; color: var(--charcoal);
  }
</style>
</head>
<body>

  <section class="card card-back">
    <p class="card-back__name">Benedikt Haufmoll</p>
  </section>

  <section class="card card-front">
    <svg class="card-front__swoosh" viewBox="0 0 560 320" preserveAspectRatio="none" aria-hidden="true">
      <path d="M110 320 C 250 300 340 185 560 150 L560 320 Z" fill="var(--charcoal)"/>
      <path d="M40 320 C 200 300 300 215 470 172 C 330 222 240 296 100 320 Z" fill="var(--lime)"/>
    </svg>

    <div class="wordmark">
      <span class="wordmark__dot"></span>
      <span class="wordmark__name">Haufmoll</span>
    </div>

    <div class="identity">
      <h1 class="identity__name">Mag. Benedikt Haufmoll</h1>
      <p class="identity__title">Energetische Praxis</p>
    </div>

    <ul class="contact">
      <li>
        <svg viewBox="0 0 16 16"><path d="M1 5c0-2 2-3 7-3s7 1 7 3v1h-4V5H5v1H1zM3 7h10l2 7H1z"/></svg>
        +43 664 5550182
      </li>
      <li>
        <svg viewBox="0 0 16 16"><path d="M1 3h14v10H1z M1 3l7 6 7-6" stroke="#fff" stroke-width="1"/></svg>
        benedikt@haufmoll.one
      </li>
      <li>
        <svg viewBox="0 0 16 16"><circle cx="8" cy="8" r="7"/><path d="M5 4l3 2-1 3 3 2 1 3" stroke="#fff" stroke-width="1.4" fill="none"/></svg>
        <span>www.<span class="accent">dlorvan</span>.net</span>
      </li>
    </ul>

    <p class="address">Birkenweg 9, 5020 Stadelried<br>Österreich</p>
  </section>

</body>
</html>
```